Postcard Design

Domestic home cleaning business.......looking to call it " copper lantern" I would like to have a vastrelo bottle as the main feature.....on the bottle the centre lable shoild read I'M YOUR ALL PURPOSE CLEANER above the lable should read DON'T LIFT A FINGER! Then opposite the bottle 5 bullet points House Keeping, Washing,Ironing bed changing, END OF TENANCY CLEANS, MOVING IN CLEANS spring cleans.

On the back of the card Iwould like to list the following: At the top of the card it should read
THE ALL PURPOSE PERSONALISED CLEANER AND WHAT YOU CAN EXPECT

Reliable
Police checked and referenced cleaners
SAME CLEANER EVERY WEEK ON THE SAME DAY AND TIME TO BE AGREED BY YOU
ONLY EVER USE CUSTOMERS OWN PRODUCTS
EACH CLEAN INSURED
GENERAL HOUSE CLEANING AS WELL AS IRONING IF REQUIRED (min 2hours per week)

Reason: I have a couple of hospital appointments to attend this week after s major operation, so I need more time to concentrate......sorry

```html
<!DOCTYPE html>
<html lang="en">
<head>
<meta charset="utf-8">
<title>Copper Lantern – Domestic Home Cleaning Postcard</title>
<link rel="stylesheet" href="https://fonts.googleapis.com/css2?family=Roboto:wght@400;500;700&family=Roboto+Condensed:wght@400;500;700&display=swap">
<style>
  :root {
    --backdrop: #e9e9e9;
    --card: #ffffff;
    --navy: #1f2f6b;
    --sky: #1f96d6;
    --band: #cfe9f8;
    --ink: #222222;
    --tick: #d42a1e;
    --web-red: #d4201a;
    --line: #bcbcbc;
  }
  * { margin: 0; padding: 0; box-sizing: border-box; }
  html, body { width: 1200px; height: 692px; overflow: hidden; background: var(--backdrop); }
  body { position: relative; font-family: "Roboto", Arial, sans-serif; color: var(--ink); }

  .card { position: absolute; background: var(--card); overflow: hidden; box-shadow: 0 2px 6px rgba(0,0,0,.18); }
  .card--front { left: 58px; top: 44px; width: 458px; height: 590px; }
  .card--back { left: 562px; top: 177px; width: 591px; height: 457px; }

  .band { position: absolute; background: linear-gradient(90deg, var(--band) 0%, var(--band) 75%, rgba(207,233,248,0) 100%); }
  .card--front .band { left: 8px; top: 40px; width: 450px; height: 78px; background: var(--band); }
  .card--back .band { left: 0; top: 25px; width: 360px; height: 72px; }

  .band-title { position: absolute; color: var(--navy); font-weight: 500; white-space: nowrap; }
  .card--front .band-title { left: 250px; top: 72px; font-size: 14.5px; }
  .card--back .band-title { left: 30px; top: 45px; font-size: 25px; font-weight: 400; }

  .product-shot { position: absolute; left: 0; top: 40px; width: 212px; height: 550px;
    border-radius: 0 60px 0 0;
    background: radial-gradient(ellipse at 50% 68%, #f7c52b 0%, #f2a81c 22%, #6fb7e8 45%, #3f9de0 70%, #d6ecfa 100%); }
  .product-shot::before { content: ""; position: absolute; left: 0; top: 0; width: 212px; height: 240px;
    border-radius: 0 60px 0 0;
    background: linear-gradient(160deg, #e0311f 0%, #f2d046 45%, rgba(242,208,70,0) 80%); }

  .headline { position: absolute; left: 225px; top: 152px; font-size: 43px; line-height: 42px; font-weight: 400; color: var(--sky); white-space: nowrap; }
  .headline .dark { color: var(--navy); }

  .checklist { position: absolute; list-style: none; }
  .checklist li { position: relative; padding-left: 11px; white-space: nowrap; }
  .checklist svg { position: absolute; left: 0; width: 7px; height: 7px; }
  .card--front .checklist { left: 243px; top: 294px; font-size: 13.5px; font-weight: 500; }
  .card--front .checklist li { height: 24px; }
  .card--front .checklist svg { top: 5px; }

  .cta { position: absolute; color: var(--sky); font-size: 12.5px; white-space: nowrap; }
  .contact { position: absolute; font-size: 9.5px; color: #444; display: flex; gap: 12px; align-items: center; white-space: nowrap; }
  .contact span { display: flex; align-items: center; gap: 4px; }
  .contact svg { width: 8px; height: 8px; }
  .web { position: absolute; color: var(--web-red); font-weight: 700; font-size: 15px; white-space: nowrap; }
  .card--front .cta { left: 260px; top: 488px; }
  .card--front .contact { left: 266px; top: 507px; }
  .card--front .web { left: 258px; top: 520px; }

  .back-heading { position: absolute; left: 30px; top: 108px; font-size: 21px; line-height: 29px; font-weight: 500; color: var(--navy); white-space: nowrap; }
  .back-heading .light { color: var(--sky); font-weight: 400; }

  .cleaner-photo { position: absolute; left: 3px; top: 182px; width: 96px; height: 275px;
    background: linear-gradient(180deg, #e7c4a6 0%, #d9a887 30%, #f4f4f4 45%, #2a63c4 60%, #1e4fa8 100%); }
  .supplies-photo { position: absolute; left: 224px; top: 287px; width: 142px; height: 170px; opacity: .35;
    background: radial-gradient(ellipse at 50% 60%, #f3d36a 0%, #a6d67d 35%, #8fc5ea 60%, rgba(255,255,255,0) 85%); }

  .reliable { position: absolute; left: 101px; top: 171px; color: var(--sky); font-style: italic; font-size: 12px; }
  .card--back .checklist { left: 101px; top: 193px; font-family: "Roboto Condensed", Arial, sans-serif; font-weight: 500; font-size: 11.5px; line-height: 14px; }
  .card--back .checklist li { margin-bottom: 7px; }
  .card--back .checklist svg { top: 3px; }

  .card--back .cta { left: 120px; top: 374px; font-size: 13px; }
  .card--back .contact { left: 126px; top: 396px; }
  .card--back .web { left: 122px; top: 410px; }

  .stamp-box { position: absolute; left: 508px; top: 25px; width: 60px; height: 40px; border: 1px solid #bbb; }
  .address-line { position: absolute; left: 383px; width: 185px; height: 0; border-top: 1.5px solid var(--line); }
</style>
</head>
<body>

<section class="card card--front" aria-label="Postcard front">
  <div class="band"></div>
  <p class="band-title">Domestic Home Cleaning</p>
  <div class="product-shot" role="img" aria-label="Gloved hand holding a blue Vastrelo spray bottle labelled Don't lift a finger! – I'm your all purpose cleaner"></div>

  <h1 class="headline"><span class="dark">I'm</span> your<br>all-purpose<br>cleaner.</h1>

  <ul class="checklist">
    <li><svg viewBox="0 0 10 10"><path d="M1 5 L4 8 L9 2" fill="none" stroke="var(--tick)" stroke-width="2"/></svg>House Keeping</li>
    <li><svg viewBox="0 0 10 10"><path d="M1 5 L4 8 L9 2" fill="none" stroke="var(--tick)" stroke-width="2"/></svg>Washing</li>
    <li><svg viewBox="0 0 10 10"><path d="M1 5 L4 8 L9 2" fill="none" stroke="var(--tick)" stroke-width="2"/></svg>Ironing bed changing</li>
    <li><svg viewBox="0 0 10 10"><path d="M1 5 L4 8 L9 2" fill="none" stroke="var(--tick)" stroke-width="2"/></svg>END OF TENANCY CLEANS</li>
    <li><svg viewBox="0 0 10 10"><path d="M1 5 L4 8 L9 2" fill="none" stroke="var(--tick)" stroke-width="2"/></svg>MOVING IN CLEANS</li>
    <li><svg viewBox="0 0 10 10"><path d="M1 5 L4 8 L9 2" fill="none" stroke="var(--tick)" stroke-width="2"/></svg>spring cleans</li>
  </ul>

  <p class="cta">Call today for your FREE estimate!</p>
  <p class="contact">
    <span><svg viewBox="0 0 10 10"><circle cx="5" cy="5" r="5" fill="var(--sky)"/></svg>000 000</span>
    <span><svg viewBox="0 0 10 10"><circle cx="5" cy="5" r="5" fill="var(--sky)"/></svg>hello@copperlantern.net</span>
  </p>
  <p class="web">www.CopperLantern.net</p>
</section>

<section class="card card--back" aria-label="Postcard back">
  <div class="band"></div>
  <p class="band-title">Domestic Home Cleaning</p>
  <div class="stamp-box"></div>
  <div class="address-line" style="top:156px"></div>
  <div class="address-line" style="top:186px"></div>
  <div class="address-line" style="top:216px"></div>
  <div class="address-line" style="top:245px"></div>
  <div class="address-line" style="top:277px"></div>

  <h2 class="back-heading">The <span class="light">all-purpose personalised</span><br><span class="light">cleaner and what</span> you can expect</h2>

  <div class="supplies-photo" role="img" aria-label="Faded bucket of cleaning supplies with spray bottles and gloves"></div>
  <div class="cleaner-photo" role="img" aria-label="Smiling cleaner in a blue apron holding a cloth"></div>

  <p class="reliable">Reliable</p>
  <ul class="checklist">
    <li><svg viewBox="0 0 10 10"><path d="M1 5 L4 8 L9 2" fill="none" stroke="var(--tick)" stroke-width="2"/></svg>Police checked and referenced cleaners</li>
    <li><svg viewBox="0 0 10 10"><path d="M1 5 L4 8 L9 2" fill="none" stroke="var(--tick)" stroke-width="2"/></svg>Same Cleaner Every Week On The Same Day<br>and Time To Be Agreed By You</li>
    <li><svg viewBox="0 0 10 10"><path d="M1 5 L4 8 L9 2" fill="none" stroke="var(--tick)" stroke-width="2"/></svg>Only Ever Use Customers Own Products</li>
    <li><svg viewBox="0 0 10 10"><path d="M1 5 L4 8 L9 2" fill="none" stroke="var(--tick)" stroke-width="2"/></svg>Each Clean Insured</li>
    <li><svg viewBox="0 0 10 10"><path d="M1 5 L4 8 L9 2" fill="none" stroke="var(--tick)" stroke-width="2"/></svg>General House Cleaning As Well As Ironing<br>If Required (Min 2hours Per Week)</li>
  </ul>

  <p class="cta">Call today for your FREE estimate!</p>
  <p class="contact">
    <span><svg viewBox="0 0 10 10"><circle cx="5" cy="5" r="5" fill="var(--sky)"/></svg>000 000</span>
    <span><svg viewBox="0 0 10 10"><circle cx="5" cy="5" r="5" fill="var(--sky)"/></svg>hello@copperlantern.net</span>
  </p>
  <p class="web">www.CopperLantern.net</p>
</section>

</body>
</html>
```